Trade show post card for sportfishing

I would like a double sided postcard used to be a larger more descriptive, eye catching, marketing tool to be used at trade show. I want the double sided postcard to be descriptive and eye catching for both avid fisherman and inviting enough not to scare away first timers looking to enjoy the experience.

Target Market(s)

Males 25-60

Colors

Designer to choose colors to be used in the design.

Requirements
Must have
• My logo, website, phone number, type of trips, pictures of fishing trips we have had which I included below. But I do not need all of the pictures designers can use ones they feel will be most appealing
Nice to have
• Color scheme that works with my logo.

```html
<!DOCTYPE html>
<html lang="en">
<head>
<meta charset="utf-8">
<title>Harbor Line Sportfishing – Trade Show Postcard</title>
<link rel="stylesheet" href="https://fonts.googleapis.com/css2?family=Lato:wght@400;700;900&family=Oswald:wght@500;700&display=swap">
<style>
  :root{
    --page:#e4e4e4;
    --ink:#0d0d0d;
    --white:#ffffff;
    --green:#5bb04a;
    --orange:#c9761f;
    --mist:#c9cccd;
    --mist-light:#eef0f0;
    --badge-text:#1a1a1a;
    --pin:#c8282b;
  }
  *{box-sizing:border-box;margin:0;padding:0}
  html,body{width:902px;height:1200px;overflow:hidden}
  body{background:var(--page);font-family:"Lato",Arial,sans-serif;position:relative}

  .postcard{position:absolute;left:41px;width:820px;height:510px;overflow:hidden;background:var(--ink);box-shadow:0 6px 18px rgba(0,0,0,.25)}
  .postcard--front{top:55px}
  .postcard--back{top:625px}
  .layer{position:absolute;inset:0}

  /* front */
  .river-photo{position:absolute;left:0;top:0;width:820px;height:230px;background:linear-gradient(180deg,#b6babb 0%,var(--mist) 45%,var(--mist-light) 100%)}
  .angler-photo{position:absolute;left:450px;top:0;width:370px;height:510px;background:radial-gradient(ellipse at 50% 55%,#9fa3a6 0%,#5b4a3d 45%,#2a201a 100%)}
  .brand{position:absolute;display:flex;align-items:center;gap:8px;font-family:"Lato",Arial,sans-serif;font-weight:900;color:var(--green);text-transform:uppercase;letter-spacing:.5px;line-height:1;white-space:nowrap}
  .brand__dot{width:14px;height:14px;border-radius:50%;background:var(--green);flex:none}
  .brand--front{left:110px;top:80px;font-size:28px}
  .headline{position:absolute;left:34px;top:208px;color:var(--white);font-family:"Oswald",Arial,sans-serif;font-weight:700;text-transform:uppercase;line-height:1}
  .headline__line1{font-size:23px;display:block}
  .headline__line2{font-size:33px;font-weight:500;display:block;margin-top:1px}
  .headline__year{position:absolute;left:300px;top:196px;font-family:"Oswald",Arial,sans-serif;font-weight:700;font-size:56px;color:var(--ink);line-height:1}
  .pricing-title{position:absolute;left:42px;top:280px;color:var(--white);font-weight:700;font-size:16px;letter-spacing:.3px}
  .ribbon{position:absolute;background:var(--ink);color:var(--white);font-weight:700;font-size:14px;padding:5px 26px 5px 12px;clip-path:polygon(0 0,100% 0,94% 50%,100% 100%,0 100%);white-space:nowrap}
  .ribbon--short{left:30px;top:306px;width:345px}
  .ribbon--full{left:30px;top:360px;width:235px}
  .trip-note{position:absolute;left:42px;color:var(--ink);font-size:11.5px;line-height:1.25}
  .trip-note--short{top:337px;width:345px}
  .trip-note--full{top:391px;width:320px}
  .price{position:absolute;width:66px;height:36px;border-radius:50%;background:var(--white);border:2px solid var(--ink);display:flex;align-items:center;justify-content:center;font-family:"Oswald",Arial,sans-serif;font-weight:700;font-size:15px;color:var(--badge-text)}
  .price--short{left:378px;top:322px}
  .price--full{left:378px;top:378px}
  .contact{position:absolute;color:var(--white);font-weight:700;line-height:1}
  .contact__row{display:flex;align-items:center;gap:10px;margin-bottom:8px;white-space:nowrap}
  .contact--front{left:48px;top:458px;font-size:15px}
  .icon{width:14px;height:14px;flex:none}

  /* back */
  .shore-photo{position:absolute;left:440px;top:0;width:380px;height:420px;background:linear-gradient(180deg,#e3e6e6 0%,#f4f5f5 50%,#d8dad9 100%)}
  .about-label{position:absolute;left:22px;top:32px;background:var(--ink);color:var(--white);font-weight:900;font-size:17px;padding:5px 34px 5px 14px;clip-path:polygon(0 0,100% 0,92% 50%,100% 100%,0 100%)}
  .about-copy{position:absolute;left:24px;top:68px;width:405px;color:var(--white);font-weight:700;font-size:10.8px;line-height:1.32}
  .about-copy p{margin-bottom:8px}
  .snapshot{position:absolute;width:150px;height:125px;border:7px solid var(--green);background:var(--white);padding:3px}
  .snapshot__fill{width:100%;height:100%}
  .snapshot--one{left:600px;top:40px;transform:rotate(2deg)}
  .snapshot--two{left:610px;top:205px;transform:rotate(-5deg)}
  .snapshot--three{left:605px;top:370px;transform:rotate(1deg)}
  .pin{position:absolute;width:10px;height:10px;border-radius:50%;background:var(--pin)}
  .brand--back{left:40px;top:458px;font-size:22px}
  .contact--back{left:215px;top:440px;font-size:15px}
  .contact__call{color:var(--green);font-weight:900;font-size:14px;margin-bottom:9px}
</style>
</head>
<body>

<section class="postcard postcard--front" aria-label="Postcard front">
  <div class="river-photo" role="img" aria-label="Misty river valley with hills in the background"></div>
  <svg class="layer" viewBox="0 0 820 510" aria-hidden="true">
    <defs>
      <linearGradient id="frontOrange" x1="0" y1="0" x2="1" y2="1">
        <stop offset="0" stop-color="#e29a3c"/>
        <stop offset=".5" stop-color="#c9761f"/>
        <stop offset="1" stop-color="#7a3f12"/>
      </linearGradient>
    </defs>
    <path d="M0 188 L60 180 L120 186 L180 166 L240 170 L300 140 L360 132 L420 105 L480 85 L540 75 L600 55 L660 38 L720 28 L820 10 L820 510 L0 510Z" fill="var(--green)"/>
    <path d="M0 195 L60 187 L120 193 L180 173 L240 177 L300 147 L360 139 L420 112 L480 92 L540 82 L600 62 L660 45 L720 35 L820 17 L820 510 L0 510Z" fill="url(#frontOrange)"/>
    <path d="M0 510 L0 442 C40 434 70 448 110 439 S190 434 240 442 S330 429 380 434 S430 440 460 432 L460 510 Z" fill="var(--green)"/>
    <path d="M0 510 L0 450 C40 442 70 456 110 447 S190 442 240 450 S330 437 380 442 S430 448 460 440 L460 510 Z" fill="var(--ink)"/>
  </svg>
  <div class="angler-photo" role="img" aria-label="Angler in a cap holding a large striped bass on a boat"></div>

  <div class="brand brand--front"><span class="brand__dot"></span>Harbor Line</div>

  <h1 class="headline"><span class="headline__line1">Hudson River Striped</span><span class="headline__line2">Bass Spring</span></h1>
  <div class="headline__year">2018</div>

  <div class="pricing-title">PRICING (APRIL &amp; MAY)</div>
  <div class="ribbon ribbon--short">Sunrise or sunset trip, 5 hours with 1-4 guests,</div>
  <p class="trip-note trip-note--short">All live bait, top of the line fishing gear and electronics.</p>
  <div class="price price--short">$500.00</div>

  <div class="ribbon ribbon--full">Full day 8 hour trip 1-4 guests,</div>
  <p class="trip-note trip-note--full">Times selected by captain to provide best opportunity to catch fish, all live bait, top of the line fishing gear and electronics</p>
  <div class="price price--full">$900.00</div>

  <div class="contact contact--front">
    <div class="contact__row">
      <svg class="icon" viewBox="0 0 24 24"><path fill="var(--white)" d="M6.6 10.8a15.1 15.1 0 0 0 6.6 6.6l2.2-2.2c.3-.3.7-.4 1-.2 1.1.4 2.3.6 3.6.6.6 0 1 .4 1 1V20c0 .6-.4 1-1 1A17 17 0 0 1 3 4c0-.6.4-1 1-1h3.5c.6 0 1 .4 1 1 0 1.3.2 2.5.6 3.6.1.3 0 .7-.2 1z"/></svg>
      (845) 555-0142
    </div>
    <div class="contact__row">
      <svg class="icon" viewBox="0 0 24 24"><circle cx="12" cy="12" r="10" fill="none" stroke="var(--white)" stroke-width="2"/><path d="M2 12h20M12 2c3 3 3 17 0 20M12 2c-3 3-3 17 0 20" fill="none" stroke="var(--white)" stroke-width="2"/></svg>
      WWW.HARBORLINESPORTFISHING.COM
    </div>
  </div>
</section>

<section class="postcard postcard--back" aria-label="Postcard back">
  <div class="shore-photo" role="img" aria-label="Faded photo of a boat deck on the river"></div>
  <svg class="layer" viewBox="0 0 820 510" aria-hidden="true">
    <defs>
      <linearGradient id="backOrange" x1="0" y1="0" x2="1" y2="1">
        <stop offset="0" stop-color="#7a3f12"/>
        <stop offset=".45" stop-color="#c9761f"/>
        <stop offset="1" stop-color="#5a2c0e"/>
      </linearGradient>
    </defs>
    <path d="M0 0 L445 0 L452 30 L440 60 L458 95 L446 130 L462 170 L450 210 L468 250 L456 290 L470 330 L462 370 L475 420 L0 420Z" fill="var(--white)"/>
    <path d="M0 0 L438 0 L445 30 L433 60 L451 95 L439 130 L455 170 L443 210 L461 250 L449 290 L463 330 L455 370 L468 420 L0 420Z" fill="url(#backOrange)"/>
    <path d="M0 408 C80 395 150 412 240 400 S420 395 520 405 S700 390 820 400 L820 510 L0 510Z" fill="var(--green)"/>
    <path d="M0 416 C80 403 150 420 240 408 S420 403 520 413 S700 398 820 408 L820 510 L0 510Z" fill="var(--ink)"/>
  </svg>

  <div class="about-label">ABOUT US</div>
  <div class="about-copy">
    <p>Captains Dan and Walt grew up in Dutchess County, New York and it did not take long for them to acknowledge the special Striped Bass fishery that exists in the Hudson River. By the age of 5 both Dan and Walt were on the Hudson River fishing as often as they could be. As time went on a deep passion for fishing developed. When they were old enough to purchase their own boats and venture out onto the river on their own, they did. Since then, they have spent thousands of hours studying these migratory fish, figuring out where they are and developing new ways to catch them.</p>
    <p>When you are fishing aboard the Osprey, you will be using top of the line custom made fishing rods specially designed for live bait fishing for striped bass. These rods are made by Ridgeback Customs, the premier rod builder in the North East! Each rod is paired perfectly with Tidecraft reels, we want our clients to experience nothing but the best, from the experience to the gear!</p>
    <p>Striped Bass Fishing with Harbor Line Sportfishing will be fun for the whole family. We love seeing kids and first timers land fish! We explain our techniques, give our clients choices in fishing styles, and we are open to questions that can help our clients understand our local fishery.</p>
  </div>

  <div class="snapshot snapshot--one"><div class="snapshot__fill" role="img" aria-label="Young angler holding a striped bass on a boat" style="background:linear-gradient(160deg,#9aa7ad,#4b4f52)"></div></div>
  <div class="snapshot snapshot--two"><div class="snapshot__fill" role="img" aria-label="Group of anglers showing off a striped bass catch" style="background:linear-gradient(160deg,#b7c3c8,#5d6366)"></div></div>
  <span class="pin" style="left:645px;top:202px"></span>
  <div class="snapshot snapshot--three"><div class="snapshot__fill" role="img" aria-label="Fishing party on the boat deck with their catch" style="background:linear-gradient(160deg,#c9d2d6,#6b6f70)"></div></div>
  <span class="pin" style="left:597px;top:366px"></span>

  <div class="brand brand--back"><span class="brand__dot"></span>Harbor Line</div>

  <div class="contact contact--back">
    <div class="contact__call">CONTACT US TODAY!</div>
    <div class="contact__row">
      <svg class="icon" viewBox="0 0 24 24"><path fill="var(--white)" d="M6.6 10.8a15.1 15.1 0 0 0 6.6 6.6l2.2-2.2c.3-.3.7-.4 1-.2 1.1.4 2.3.6 3.6.6.6 0 1 .4 1 1V20c0 .6-.4 1-1 1A17 17 0 0 1 3 4c0-.6.4-1 1-1h3.5c.6 0 1 .4 1 1 0 1.3.2 2.5.6 3.6.1.3 0 .7-.2 1z"/></svg>
      (845) 555-0142
    </div>
    <div class="contact__row">
      <svg class="icon" viewBox="0 0 24 24"><circle cx="12" cy="12" r="10" fill="none" stroke="var(--white)" stroke-width="2"/><path d="M2 12h20M12 2c3 3 3 17 0 20M12 2c-3 3-3 17 0 20" fill="none" stroke="var(--white)" stroke-width="2"/></svg>
      WWW.HARBORLINESPORTFISHING.COM
    </div>
  </div>
</section>

</body>
</html>
```